business card design for a small scale specialty cut flower farm

We need a business card design for Hollowmere Bloom Farm based in Langley, BC, Canada. We produce specialty, high-end cut flowers and sell locally to florists, local shops and markets and the end user through bouquet subscriptions. The final business card design should be memorable and have a timeless or vintage feel. We would prefer a square shape.
Updates

Target Market(s)

florists, shops and seasonal markets, local flower lovers

Industry/Entity Type

Floral

Contact Information for Business Card

Tamsin Ellery Voss, Grower
Langley, BC, Canada
website: hollowmerebloomfarm.example
instagram: @hollowmerebloomfarm
Tel: 555.317.4290
facebook: www.facebook.example/hollowmereblooms/

Font styles to use
Serif
Decorative
Script

Requirements
Must have
• soft black background colour on front side, the included logo and catch phrase: Fresh Local Seasonal
Nice to have
• phone number and website address on front of card, included photo 6539 incorporated onto the back, possibly photo 6609 as well.

```html
<!DOCTYPE html>
<html lang="en">
<head>
<meta charset="utf-8">
<title>Hollowmere Bloom Farm – Business Cards</title>
<link href="https://fonts.googleapis.com/css2?family=Allura&family=Lato:wght@400;700&family=Cormorant+Garamond:wght@500&display=swap" rel="stylesheet">
<style>
  :root {
    --backdrop: #1c1c1d;
    --card: #2e2e30;
    --ink: #f4f2ef;
    --leaf: #74a065;
    --rose: #d97aa8;
    --icon: #8fb483;
  }
  * { box-sizing: border-box; margin: 0; padding: 0; }
  html, body { width: 1200px; height: 900px; overflow: hidden; background: var(--backdrop); }
  .canvas { position: relative; width: 1200px; height: 900px; }
  .card {
    position: absolute; left: 240px; width: 720px; height: 400px;
    background: var(--card); overflow: hidden; color: var(--ink);
    font-family: "Lato", sans-serif;
  }
  .card--front { top: 30px; }
  .card--back { top: 470px; }

  .brand-name {
    font-family: "Cormorant Garamond", serif; font-weight: 500;
    color: var(--ink); text-transform: uppercase; letter-spacing: 0.14em;
    line-height: 1.05; text-align: center;
  }
  .card--front .brand-name { position: absolute; top: 118px; left: 0; right: 0; font-size: 46px; }
  .card--front .brand-name span { display: block; font-size: 30px; letter-spacing: 0.3em; margin-top: 10px; }

  .front-footer { position: absolute; left: 40px; right: 40px; bottom: 34px; display: flex; justify-content: space-between; align-items: flex-end; font-size: 17px; }
  .front-footer .phone { align-self: flex-start; margin-bottom: 12px; }
  .tagline { color: var(--leaf); text-transform: uppercase; font-size: 17px; letter-spacing: 0.03em; }

  .card--back .brand-name { position: absolute; top: 48px; left: 60px; width: 320px; font-size: 30px; }
  .card--back .brand-name span { display: block; font-size: 20px; letter-spacing: 0.3em; margin-top: 8px; }

  .person { position: absolute; top: 170px; left: 62px; padding-left: 24px; border-left: 7px solid var(--rose); }
  .person-name { font-family: "Allura", cursive; color: var(--leaf); font-size: 40px; line-height: 1; }
  .person-role { font-size: 17px; margin-top: 4px; }

  .contact-list { position: absolute; top: 262px; left: 62px; list-style: none; font-size: 17px; line-height: 27px; }
  .contact-list li { display: flex; align-items: center; gap: 10px; white-space: nowrap; }
  .contact-list svg { width: 16px; height: 16px; flex: none; }

  .back-art { position: absolute; inset: 0; width: 720px; height: 400px; }
</style>
</head>
<body>
<div class="canvas">

  <section class="card card--front">
    <h1 class="brand-name">Hollowmere<span>Bloom Farm</span></h1>
    <div class="front-footer">
      <span class="phone">(555) 317-4290</span>
      <span class="tagline">Fresh Local Seasonal</span>
      <span class="website">hollowmerebloomfarm.example</span>
    </div>
  </section>

  <section class="card card--back">
    <svg class="back-art" viewBox="0 0 720 400">
      <defs>
        <linearGradient id="bloomTones" x1="0" y1="0" x2="1" y2="1">
          <stop offset="0" stop-color="#7a5fc0"/>
          <stop offset="0.35" stop-color="#d8507a"/>
          <stop offset="0.65" stop-color="#8a2a4a"/>
          <stop offset="1" stop-color="#c9d3de"/>
        </linearGradient>
      </defs>
      <path class="accent-swoosh" fill="var(--rose)" d="M402,190 C402,280 418,350 446,400 H470 C440,340 420,270 420,190 Z"/>
      <path role="img" aria-label="Photo of a galvanised bucket of pink and burgundy dahlias with hydrangeas and purple delphiniums" fill="url(#bloomTones)" d="M415,0 H720 V400 H476 C440,330 418,250 418,150 C418,90 416,40 415,0 Z"/>
    </svg>

    <h2 class="brand-name">Hollowmere<span>Bloom Farm</span></h2>

    <div class="person">
      <p class="person-name">Tamsin Ellery Voss</p>
      <p class="person-role">Owner</p>
    </div>

    <ul class="contact-list">
      <li>
        <svg viewBox="0 0 16 16"><path fill="var(--icon)" d="M4 1.5l2.2 2.8-1.3 1.6c.8 1.9 2.3 3.4 4.2 4.2l1.6-1.3 2.8 2.2-1.5 2.5C7 13.5 2.5 9 1.5 3z"/></svg>
        (555) 317-4290
      </li>
      <li>
        <svg viewBox="0 0 16 16"><circle cx="8" cy="8" r="7" fill="var(--icon)"/></svg>
        @hollowmerebloomfarm
      </li>
      <li>
        <svg viewBox="0 0 16 16"><rect x="1.5" y="1.5" width="13" height="13" rx="2" fill="var(--icon)"/></svg>
        social.example/hollowmereblooms/
      </li>
      <li>
        <svg viewBox="0 0 16 16"><g fill="none" stroke="var(--icon)" stroke-width="1.4"><circle cx="8" cy="8" r="6.5"/><ellipse cx="8" cy="8" rx="3" ry="6.5"/><path d="M1.5 8h13"/></g></svg>
        www.hollowmerebloomfarm.example
      </li>
    </ul>
  </section>

</div>
</body>
</html>
```